Travel Itinerary Planning Website Redesign

We have built our own website for a travel itinerary planning service using Wix but are not professional designers. We need help getting over the finish line with a redesign of our website. <br/><br/>We like material design elements, icons and styling. The pages need to flow well one to another and evoke a sense of exclusivity, without giving the impression that it's unattainable. The website doesn't need to keep its current "boxy" format but instead should have a better aesthetic and flow. We're also looking for a complete redesign of the "How It Works" section (shown on two different pages of the website) to be more visually pleasing and easy to understand (maybe using icons or infographic style people). <br/><br/>We already have our logo and selected colors. The copy is also available on the live site as well. The redesign will focus on 4 pages: the homepage and the three service pages (one page per service). The website is currently live at www.trelmavista.com. Fonts should be Helvetica Bold, Regular and Light. Preferred color scheme is attached.

Target Market(s)

Ages 28-65, living in the US, mostly large cities with a desire for well planned, non-group travels

Industry/Entity Type

Travel Industry

Font styles to use
Other font styles liked:
• Helvetica

Colors

Designer to choose colors to be used in the design.

Requirements
Must have
• Make sure to use colors we provided in the attachment and what's on the current website
• Redesign "How it Works"
• Include ambassadors area
• Have a second page that showcases how the "Personal Trip Planning" page should look
Should not have
• No header menu needed for this project

```html
<!DOCTYPE html>
<html lang="en">
<head>
<meta charset="utf-8">
<title>TrelmaVista – Tailored Travel Itineraries</title>
<link href="https://fonts.googleapis.com/css2?family=Arimo:wght@400;700&family=Inter:wght@300;400&display=swap" rel="stylesheet">
<style>
:root{
  --gold:#c9a04a;
  --brown:#7a5a1f;
  --sun:#ffd27d;
  --sun-soft:#ffe2a8;
  --paper:#f8f8f8;
  --white:#ffffff;
  --ink:#222222;
  --muted:#e2b462;
}
*{margin:0;padding:0;box-sizing:border-box}
html,body{width:1200px;height:2954px;overflow:hidden}
body{position:relative;font-family:"Arimo",Helvetica,Arial,sans-serif;color:var(--ink);background:var(--paper)}
.abs{position:absolute}
.line1{line-height:1}

/* hero */
.hero{left:0;top:0;width:1200px;height:367px;
  background:linear-gradient(180deg,#3e3f6e 0%,#7b5a8e 30%,#c56f8e 48%,#8b6c93 62%,#3b4468 82%,#22283f 100%)}
.brand-name{font-weight:700;color:var(--white);font-size:27px;letter-spacing:1px}
.nav a{position:absolute;top:42px;color:var(--white);font-size:13px;text-decoration:none;line-height:1}
.nav .active{border-bottom:2px solid var(--white);padding-bottom:6px}
.hero-title{left:0;width:1200px;text-align:center;color:var(--white)}
.hero-title.light{top:122px;font-family:"Inter",Helvetica,sans-serif;font-weight:300;font-size:57px}
.hero-title.bold{top:181px;font-weight:700;font-size:60px}
.dots{left:572px;top:333px;display:flex;gap:5px}
.dots span{width:10px;height:10px;border-radius:50%;background:rgba(255,255,255,.45)}
.dots span.on{background:var(--white)}

/* intro */
.intro-title{left:94px;top:477px;color:var(--gold);font-weight:700;font-size:39px;line-height:35px}
.intro-text{left:94px;top:555px;font-size:16px}
.pill{border:2px solid var(--gold);border-radius:30px;color:var(--gold);display:flex;align-items:center;justify-content:center;gap:8px;font-weight:700}
.pill svg{flex:none}
.start-btn{left:905px;top:494px;width:200px;height:47px;font-size:16px}
.divider{left:94px;top:673px;width:1013px;height:2px;background:var(--sun)}

.eyebrow{font-size:15px;color:var(--ink)}
.section-title{font-weight:700;font-size:39px;line-height:35px}
.process-eyebrow{left:94px;top:730px}
.process-title{left:94px;top:752px;color:var(--gold)}

.step-card{width:207px;height:218px;top:917px;background:var(--white);border-radius:8px;box-shadow:0 2px 6px rgba(0,0,0,.12)}
.step-num{top:848px;font-weight:700;font-size:104px;color:var(--sun);line-height:1}
.step-icon{top:855px;width:84px;height:92px;border-radius:10px;background:linear-gradient(160deg,var(--sun-soft),#f3d493)}
.step-title{font-weight:700;font-size:16px;line-height:17px;color:var(--brown);left:22px;top:73px}
.step-go{left:121px;top:78px}
.step-text{left:22px;top:123px;width:172px;font-size:12px;line-height:15px;color:var(--gold)}

/* pricing */
.pricing{left:0;top:1254px;width:1200px;height:722px;background:var(--sun)}
.pricing-eyebrow{left:94px;top:1306px}
.pricing-title{left:94px;top:1330px;color:var(--brown)}
.plan{background:var(--white);border-radius:16px;box-shadow:0 2px 8px rgba(0,0,0,.1)}
.plan.standard{left:259px;top:1439px;width:292px;height:439px}
.plan.premium{left:588px;top:1358px;width:353px;height:558px;border:2px solid #f6df6a}
.avatar{border-radius:50%;background:radial-gradient(circle at 50% 40%,#ffc85a,#f0b53e)}
.plan-name{width:100%;text-align:center;font-weight:700;font-size:22px;color:var(--brown)}
.plan-price{width:100%;text-align:center;font-size:12px;color:var(--brown)}
.plan-price b{font-weight:700}
.features{list-style:none}
.features li{display:flex;align-items:center;color:var(--brown)}
.features li svg{flex:none}
.standard .features li{height:25.7px;font-size:9.5px;gap:9px}
.premium .features li{height:35.4px;font-size:11px;gap:12px}
.plan-btn{font-size:10.5px;font-weight:400;letter-spacing:.3px}

/* ambassadors */
.ambassadors{left:0;top:1976px;width:1200px;height:648px;background:var(--white)}
.portrait{left:0;top:1976px;width:528px;height:648px;background:linear-gradient(160deg,#a9c3d9 0%,#8fa9bd 45%,#b57b56 60%,#6f7b88 100%)}
.amb-eyebrow{left:585px;top:2018px;font-size:12.5px;line-height:14px}
.amb-title{left:585px;top:2052px;color:var(--brown)}
.amb-text{left:585px;top:2135px;font-size:12.5px;line-height:15px}
.quote-box{left:462px;top:2230px;width:738px;height:284px;background:var(--sun)}
.quote-mark{font-family:Georgia,serif;font-weight:700;font-size:76px;color:var(--muted);line-height:1}
.quote-text{left:119px;top:58px;font-family:"Inter",Helvetica,sans-serif;font-weight:300;font-size:31px;line-height:37px;color:var(--brown)}
.quote-text b{font-family:"Arimo",Helvetica,sans-serif;font-weight:700}
.quote-name{left:466px;top:211px;font-weight:700;font-size:18px;color:var(--brown)}
.quote-role{left:466px;top:233px;font-family:"Inter",Helvetica,sans-serif;font-weight:300;font-size:18px;color:#e7b158}
.view-btn{left:585px;top:2546px;width:181px;height:37px;font-size:11.5px;font-weight:400}

/* footer */
.footer{left:0;top:2624px;width:1200px;height:330px;background:var(--sun)}
.foot-name{left:96px;top:2848px;width:140px;text-align:center;font-weight:700;font-size:19px;color:var(--brown);letter-spacing:.5px}
.foot-mark{left:126px;top:2715px;width:80px;height:80px;border-radius:50%;background:var(--brown)}
.vrule{top:2698px;width:1px;height:181px;background:var(--brown)}
.foot-head{font-weight:700;font-size:15px;color:var(--brown)}
.foot-list{list-style:none}
.foot-list li{font-size:12.5px;height:28px;color:var(--brown)}
.foot-text{font-size:13px;line-height:19px;color:var(--brown);width:210px}
.social li{display:flex;align-items:center;gap:6px;height:31px;font-size:12.5px;color:var(--brown)}
.copyright{left:873px;top:2867px;font-size:12px;color:var(--brown)}
</style>
</head>
<body>

<!-- Hero -->
<header class="abs hero" role="img" aria-label="Sunset over a calm lake with a wooden boat"></header>
<div class="abs brand-name line1" style="left:95px;top:40px">TRELMAVISTA</div>
<nav class="nav">
  <a class="active" style="left:896px">HOME</a>
  <a style="left:968px">ABOUT</a>
  <a style="left:1046px">CONTACT</a>
</nav>
<div class="abs hero-title light line1">Keep it unique,</div>
<div class="abs hero-title bold line1">Keep it personal.</div>
<div class="abs dots"><span></span><span class="on"></span><span></span><span></span></div>

<!-- Intro -->
<h2 class="abs intro-title">Based on your needs,<br>budgets &amp; constraints.</h2>
<p class="abs intro-text line1">TrelmaVista travel engineer will work to create a tailored itinerary for you</p>
<div class="abs pill start-btn">Let’s get started!
  <svg width="13" height="13" viewBox="0 0 14 14"><circle cx="7" cy="7" r="6" fill="none" stroke="currentColor" stroke-width="1.3"/><path d="M4 7h6M7.5 4.5L10 7 7.5 9.5" fill="none" stroke="currentColor" stroke-width="1.3"/></svg>
</div>
<div class="abs divider"></div>

<!-- Process -->
<p class="abs eyebrow process-eyebrow line1">OUR PROCESS</p>
<h2 class="abs section-title process-title">How the<br>planning works</h2>

<div class="abs step-card" style="left:147px">
  <div class="abs step-title">Share your<br>references</div>
  <svg class="abs step-go" width="23" height="23" viewBox="0 0 24 24"><circle cx="12" cy="12" r="12" fill="var(--sun)"/><path d="M10 7l5 5-5 5" fill="none" stroke="#fff" stroke-width="2"/></svg>
  <p class="abs step-text">Connect with a TrelmaVista Travel Engineer and discuss your expectations, needs, and budget.</p>
</div>
<div class="abs step-card" style="left:382px">
  <div class="abs step-title" style="top:76px">Let us do<br>the work</div>
  <svg class="abs step-go" width="23" height="23" viewBox="0 0 24 24"><circle cx="12" cy="12" r="12" fill="var(--sun)"/><path d="M10 7l5 5-5 5" fill="none" stroke="#fff" stroke-width="2"/></svg>
  <p class="abs step-text" style="top:130px">Our teams will be hard at work handcrafting plans, ahead of your next departure.</p>
</div>
<div class="abs step-card" style="left:613px">
  <div class="abs step-title" style="top:76px">Obtain your<br>itinerary</div>
  <svg class="abs step-go" width="23" height="23" viewBox="0 0 24 24"><circle cx="12" cy="12" r="12" fill="var(--sun)"/><path d="M10 7l5 5-5 5" fill="none" stroke="#fff" stroke-width="2"/></svg>
  <p class="abs step-text" style="top:130px">Access a personal, digital itinerary through your favorite devices.</p>
</div>
<div class="abs step-card" style="left:851px">
  <div class="abs step-title" style="top:76px">Save time<br>and money</div>
  <svg class="abs step-go" width="23" height="23" viewBox="0 0 24 24"><circle cx="12" cy="12" r="12" fill="var(--sun)"/><path d="M10 7l5 5-5 5" fill="none" stroke="#fff" stroke-width="2"/></svg>
  <p class="abs step-text" style="top:130px">Avoid common mistakes and travel planning frustrations. We’ve got you covered.</p>
</div>

<!-- step illustrations (placeholders) -->
<div class="abs step-icon" style="left:210px" role="img" aria-label="Illustration of a light bulb idea"></div>
<div class="abs step-icon" style="left:440px;width:96px" role="img" aria-label="Illustration of a handshake"></div>
<div class="abs step-icon" style="left:676px" role="img" aria-label="Illustration of a checklist with a pointing hand"></div>
<div class="abs step-icon" style="left:911px;width:88px;height:82px" role="img" aria-label="Illustration of a wallet"></div>

<div class="abs step-num" style="left:146px">1</div>
<div class="abs step-num" style="left:383px">2</div>
<div class="abs step-num" style="left:614px">3</div>
<div class="abs step-num" style="left:851px">4</div>

<!-- Pricing -->
<section class="abs pricing"></section>
<p class="abs eyebrow pricing-eyebrow line1">SELECT A SUITABLE PLAN FOR YOU</p>
<h2 class="abs section-title pricing-title">Plans &amp; Pricing</h2>

<article class="abs plan standard">
  <div class="abs avatar" style="left:90px;top:17px;width:108px;height:108px" role="img" aria-label="Cartoon mascot wearing sunglasses and a red scarf"></div>
  <h3 class="abs plan-name line1" style="top:145px">Standard Trip</h3>
  <p class="abs plan-price line1" style="top:171px"><b>30 USD</b> / Travel Day</p>
  <ul class="abs features" style="left:42px;top:196px">
    <li><svg width="13" height="13" viewBox="0 0 14 14"><circle cx="7" cy="7" r="7" fill="var(--brown)"/><path d="M4 7.2l2 2 4-4" fill="none" stroke="#fff" stroke-width="1.6"/></svg>Personalized, hand-crafted itinerary</li>
    <li><svg width="13" height="13" viewBox="0 0 14 14"><circle cx="7" cy="7" r="7" fill="var(--brown)"/><path d="M4 7.2l2 2 4-4" fill="none" stroke="#fff" stroke-width="1.6"/></svg>Unlimited chat with a travel engineer</li>
    <li><svg width="13" height="13" viewBox="0 0 14 14"><circle cx="7" cy="7" r="7" fill="var(--brown)"/><path d="M4 7.2l2 2 4-4" fill="none" stroke="#fff" stroke-width="1.6"/></svg>20-minute kick-off call with TrelmaVista</li>
    <li><svg width="13" height="13" viewBox="0 0 14 14"><circle cx="7" cy="7" r="7" fill="var(--brown)"/><path d="M4 7.2l2 2 4-4" fill="none" stroke="#fff" stroke-width="1.6"/></svg>Lodging, food &amp; entertainment recommendations</li>
    <li><svg width="13" height="13" viewBox="0 0 14 14"><circle cx="7" cy="7" r="7" fill="var(--brown)"/><path d="M4 7.2l2 2 4-4" fill="none" stroke="#fff" stroke-width="1.6"/></svg>Access to user-friendly, online itinerary tool</li>
    <li><svg width="13" height="13" viewBox="0 0 14 14"><circle cx="7" cy="7" r="7" fill="var(--brown)"/><path d="M4 7.2l2 2 4-4" fill="none" stroke="#fff" stroke-width="1.6"/></svg>Initial itinerary delivered in 2 weeks</li>
  </ul>
  <div class="abs pill plan-btn" style="left:68px;top:380px;width:155px;height:36px">GET STARTED
    <svg width="12" height="12" viewBox="0 0 14 14"><circle cx="7" cy="7" r="6" fill="none" stroke="currentColor" stroke-width="1.3"/><path d="M4 7h6M7.5 4.5L10 7 7.5 9.5" fill="none" stroke="currentColor" stroke-width="1.3"/></svg>
  </div>
</article>

<article class="abs plan premium">
  <div class="abs avatar" style="left:122px;top:28px;width:108px;height:108px" role="img" aria-label="Cartoon mascot in a safari hat and neckerchief"></div>
  <h3 class="abs plan-name line1" style="top:186px">Premium Trip</h3>
  <p class="abs plan-price line1" style="top:207px"><b>60 USD</b> / Travel Day</p>
  <ul class="abs features" style="left:48px;top:240px">
    <li><svg width="14" height="14" viewBox="0 0 14 14"><circle cx="7" cy="7" r="7" fill="var(--brown)"/><path d="M4 7.2l2 2 4-4" fill="none" stroke="#fff" stroke-width="1.6"/></svg><b>Standard Plan + the following premium services:</b></li>
    <li><svg width="14" height="14" viewBox="0 0 14 14"><circle cx="7" cy="7" r="7" fill="var(--brown)"/><path d="M4 7.2l2 2 4-4" fill="none" stroke="#fff" stroke-width="1.6"/></svg>Flight bookings</li>
    <li><svg width="14" height="14" viewBox="0 0 14 14"><circle cx="7" cy="7" r="7" fill="var(--brown)"/><path d="M4 7.2l2 2 4-4" fill="none" stroke="#fff" stroke-width="1.6"/></svg>Accommodations negotiation and reservations</li>
    <li><svg width="14" height="14" viewBox="0 0 14 14"><circle cx="7" cy="7" r="7" fill="var(--brown)"/><path d="M4 7.2l2 2 4-4" fill="none" stroke="#fff" stroke-width="1.6"/></svg>Restaurant and activity reservations</li>
    <li><svg width="14" height="14" viewBox="0 0 14 14"><circle cx="7" cy="7" r="7" fill="var(--brown)"/><path d="M4 7.2l2 2 4-4" fill="none" stroke="#fff" stroke-width="1.6"/></svg>Concierge service</li>
    <li><svg width="14" height="14" viewBox="0 0 14 14"><circle cx="7" cy="7" r="7" fill="var(--brown)"/><path d="M4 7.2l2 2 4-4" fill="none" stroke="#fff" stroke-width="1.6"/></svg>Traveler’s itinerary booklet</li>
  </ul>
  <div class="abs pill plan-btn" style="left:100px;top:485px;width:156px;height:37px">GET STARTED
    <svg width="12" height="12" viewBox="0 0 14 14"><circle cx="7" cy="7" r="6" fill="none" stroke="currentColor" stroke-width="1.3"/><path d="M4 7h6M7.5 4.5L10 7 7.5 9.5" fill="none" stroke="currentColor" stroke-width="1.3"/></svg>
  </div>
</article>

<!-- Ambassadors -->
<section class="abs ambassadors"></section>
<div class="abs portrait" role="img" aria-label="Portrait of a brand ambassador outdoors by a lake"></div>
<p class="abs amb-eyebrow">EXPERIENCES CURATED<br>WITH INSPIRATION FROM</p>
<h2 class="abs section-title amb-title">Our Brand<br>Ambassadors</h2>
<p class="abs amb-text">Get a personalised list of the things you want to do<br>and the places you want to visit.</p>

<div class="abs quote-box">
  <span class="abs quote-mark" style="left:93px;top:38px">“</span>
  <p class="abs quote-text">Enter my testimonial<br>for <b>TrelmaVista right<br>here.</b></p>
  <span class="abs quote-mark" style="left:190px;top:122px">”</span>
  <svg class="abs" style="left:678px;top:116px" width="24" height="44" viewBox="0 0 24 44"><path d="M3 2l18 20L3 42" fill="none" stroke="var(--gold)" stroke-width="2"/></svg>
  <p class="abs quote-name line1">COLETTE VARENNE</p>
  <p class="abs quote-role line1">French Lifestyle Influencer</p>
</div>

<div class="abs pill view-btn">View all ambassadors
  <svg width="12" height="12" viewBox="0 0 14 14"><circle cx="7" cy="7" r="6" fill="none" stroke="currentColor" stroke-width="1.3"/><path d="M4 7h6M7.5 4.5L10 7 7.5 9.5" fill="none" stroke="currentColor" stroke-width="1.3"/></svg>
</div>

<!-- Footer -->
<footer class="abs footer"></footer>
<div class="abs foot-mark"></div>
<div class="abs foot-name line1">TRELMAVISTA</div>
<div class="abs vrule" style="left:285px"></div>
<div class="abs vrule" style="left:544px"></div>
<div class="abs vrule" style="left:842px"></div>

<h4 class="abs foot-head line1" style="left:317px;top:2695px">MENU</h4>
<ul class="abs foot-list" style="left:317px;top:2726px">
  <li>PERSONAL TRIP PLANNING</li>
  <li>BUSINESS TRIP PLANNING</li>
  <li>OVERSEAS EVENT PLANNING</li>
  <li>FREE TRAVEL RESOURCES</li>
  <li>TERMS AND CONDITIONS</li>
  <li>PRIVACY POLICY</li>
</ul>

<h4 class="abs foot-head line1" style="left:588px;top:2695px">WHO WE ARE</h4>
<p class="abs foot-text" style="left:588px;top:2720px">TrelmaVista’s mission is to engineer personalized, handcrafted travel itineraries and event plans for travelers worldwide</p>
<ul class="abs foot-list" style="left:588px;top:2838px">
  <li>SAMPLE LINK</li>
  <li>SAMPLE LINK</li>
</ul>

<h4 class="abs foot-head line1" style="left:873px;top:2695px">WE’RE SOCIAL!</h4>
<ul class="abs foot-list social" style="left:873px;top:2714px">
  <li><svg width="17" height="17" viewBox="0 0 18 18"><circle cx="9" cy="9" r="7.5" fill="none" stroke="var(--brown)" stroke-width="1.6"/></svg>FOLLOW US ON SNAPWALL</li>
  <li><svg width="17" height="17" viewBox="0 0 18 18"><circle cx="9" cy="9" r="8.5" fill="var(--brown)"/><path d="M6.6 7a2.4 2.4 0 1 1 3.4 2.2c-.7.4-1 .8-1 1.6" fill="none" stroke="var(--sun)" stroke-width="1.6"/><circle cx="9" cy="13.3" r="1" fill="var(--sun)"/></svg>GOT QUESTIONS? CONTACT US.</li>
</ul>
<p class="abs copyright line1">©2020 TrelmaVista I All Rights Reserved.</p>

</body>
</html>
```